A new healing and spiritual podcast needs a design.

We need a design for the podcast that will also be used on the supporting website. The name is Still Lantern Path. The podcast will be about tapping into our own guidance to have a great life. There will be interviews, meditations, discussions on all aspects of energy healing and alternative healing techniques. The website will be where classes will be offered. Looking for something that conveys a peaceful feeling without looking too "healy-feely". Yet also want it to get peoples attention.

Target Market(s)

Metaphysical, spiritual (not religious), energy healers

Font styles to use
Serif

Requirements
Must have
• The name "Still Lantern Path"
Nice to have
• I'd like it to be inviting, catch peoples eye, convey a peaceful feeling, yet not be boring.
Should not have
• Animated (like comic strip) images.

```html
<!DOCTYPE html>
<html lang="en">
<head>
<meta charset="utf-8">
<title>Still Lantern Path — Podcast Cover</title>
<link rel="stylesheet" href="https://fonts.googleapis.com/css2?family=Lato:wght@400;900&display=swap">
<style>
  :root {
    --ink-deep: #010308;
    --ink-navy: #06122a;
    --teal-dark: #062a2c;
    --teal-mid: #0d3f34;
    --gold: #d5b764;
    --gold-bright: #f3d46a;
    --bronze: #8a5a22;
    --frame-green: #86d38c;
    --frame-olive: #8a8a2a;
    --frame-orange: #c8661c;
  }
  * { margin: 0; padding: 0; box-sizing: border-box; }
  html, body {
    width: 1200px;
    height: 1200px;
    overflow: hidden;
    background: var(--ink-deep);
  }
  .cover {
    position: relative;
    width: 1200px;
    height: 1200px;
    overflow: hidden;
    font-family: "Lato", "Helvetica Neue", Arial, sans-serif;
    color: var(--gold);
  }
  .cover__art {
    position: absolute;
    inset: 0;
    width: 1200px;
    height: 1200px;
  }
  .title-block {
    position: absolute;
    left: 289px;
    top: 309px;
    width: 762px;
    height: 366px;
    border-top: 2px solid var(--gold);
    border-bottom: 2px solid var(--gold);
    display: flex;
    flex-direction: column;
    align-items: flex-end;
  }
  .title__top {
    display: flex;
    align-items: baseline;
    gap: 22px;
    margin-top: 30px;
    line-height: 1;
  }
  .title__small {
    font-weight: 400;
    font-size: 62px;
    letter-spacing: 0.02em;
    text-transform: uppercase;
  }
  .title__large {
    font-weight: 400;
    font-size: 124px;
    letter-spacing: 0.04em;
    text-transform: uppercase;
    margin-right: -5px;
  }
  .title__bold {
    font-weight: 900;
    font-size: 182px;
    line-height: 1;
    letter-spacing: 0.1em;
    margin-right: -18px;
    margin-top: 6px;
    text-transform: uppercase;
  }
  .byline {
    position: absolute;
    right: 150px;
    top: 712px;
    display: flex;
    align-items: baseline;
    gap: 18px;
    line-height: 1;
  }
  .byline__by { font-size: 36px; font-weight: 400; }
  .byline__name {
    font-size: 54px;
    font-weight: 400;
    letter-spacing: 0.03em;
    text-transform: uppercase;
  }
</style>
</head>
<body>
<main class="cover">
  <svg class="cover__art" viewBox="0 0 1200 1200" xmlns="http://www.w3.org/2000/svg">
    <defs>
      <linearGradient id="bg-wash" x1="0" y1="0" x2="1" y2="1">
        <stop offset="0" stop-color="#06282a"/>
        <stop offset="0.45" stop-color="#020910"/>
        <stop offset="1" stop-color="#010308"/>
      </linearGradient>
      <radialGradient id="pattern-glow" cx="0" cy="0.39" r="0.75">
        <stop offset="0" stop-color="#0f4a3a" stop-opacity="0.75"/>
        <stop offset="0.55" stop-color="#0a3027" stop-opacity="0.45"/>
        <stop offset="1" stop-color="#041216" stop-opacity="0"/>
      </radialGradient>
      <linearGradient id="frame-line" x1="0" y1="0" x2="1" y2="1">
        <stop offset="0" stop-color="#1f6a3c"/>
        <stop offset="0.35" stop-color="#86d38c"/>
        <stop offset="0.6" stop-color="#8a8a2a"/>
        <stop offset="1" stop-color="#c8661c"/>
      </linearGradient>
      <linearGradient id="medallion-ring" x1="0" y1="0" x2="1" y2="1">
        <stop offset="0" stop-color="#8a5a22"/>
        <stop offset="0.5" stop-color="#e7c35c"/>
        <stop offset="1" stop-color="#f3d46a"/>
      </linearGradient>
      <radialGradient id="medallion-fill" cx="0.2" cy="0.5" r="0.8">
        <stop offset="0" stop-color="#5a5a2a"/>
        <stop offset="0.6" stop-color="#123a34"/>
        <stop offset="1" stop-color="#062a2c"/>
      </radialGradient>
    </defs>

    <rect class="bg" width="1200" height="1200" fill="url(#bg-wash)"/>

    <rect class="frame" x="18" y="30" width="1142" height="1142" fill="none" stroke="url(#frame-line)" stroke-width="5"/>

    <path role="img" aria-label="Large ornamental mandala pattern in deep green, fanning out from the left edge"
          d="M18 33 H680 C700 200 640 260 640 330 C760 380 900 460 960 472 C900 490 760 560 640 620 C640 700 700 760 680 900 C600 1000 540 1100 500 1170 H18 Z"
          fill="url(#pattern-glow)"/>

    <g class="medallion">
      <circle cx="0" cy="472" r="212" fill="var(--ink-navy)"/>
      <circle cx="0" cy="472" r="200" fill="none" stroke="url(#medallion-ring)" stroke-width="5"/>
      <circle cx="0" cy="472" r="188" fill="url(#medallion-fill)" stroke="url(#medallion-ring)" stroke-width="3"
              role="img" aria-label="Gold mandala medallion with leaf-shaped petals"/>
    </g>
  </svg>

  <header class="title-block">
    <h1 class="title">
      <span class="title__top">
        <span class="title__small">Still</span>
        <span class="title__large">Lantern</span>
      </span>
    </h1>
    <span class="title__bold">Path</span>
  </header>

  <p class="byline">
    <span class="byline__by">by</span>
    <span class="byline__name">Mara Ellison</span>
  </p>
</main>
</body>
</html>
```